A guide to healing depression needs a great cover

An experienced therapist and former patient have put together a great guide to help people living with depression and their loved ones.
With the extraordinary combination of real case studies, checklists, clearly formulated medical content, helpful and detailed steps and practical exercises, everyone can learn how to put their own life back on the right track. We put an end to the constant worries, rebuild your self-esteem and start with positive thoughts into a happy future.
We imagine the sufferer coming out of the darkness and walking into the sunrise (or something like that). A very bright cover, which symbolizes light, would also be possible. Attached you will find an image that appealed to us, but which seems too cheap.

Target Market(s)

Depressed people and their families

Font styles to use
Serif

Requirements
Must have
• go from darkness into light
Nice to have
• For the title, it would be great if the word depression were highlighted
Should not have
• don't look cheap

```html
<!DOCTYPE html>
<html lang="de">
<head>
<meta charset="utf-8">
<title>Hallo Depression, Schluss! – Buchcover</title>
<link href="https://fonts.googleapis.com/css2?family=Bebas+Neue&family=Josefin+Sans:wght@400;700&display=swap" rel="stylesheet">
<style>
  :root {
    --stage: #e0dfe3;
    --ink: #141414;
    --title-blue: #0b45a0;
    --sky-deep: #1d4b6e;
    --sky-cyan: #4fa6c4;
    --cloud-light: #dfe9dc;
    --sun-cream: #f7f3d0;
    --ground-dusk: #3a3550;
    --ground-green: #2f4a3c;
    --author-white: #ffffff;
  }
  * { margin: 0; padding: 0; box-sizing: border-box; }
  html, body {
    width: 1200px;
    height: 955px;
    overflow: hidden;
    background: var(--stage);
  }
  .stage {
    width: 1200px;
    height: 955px;
    display: flex;
    align-items: center;
    justify-content: center;
  }
  .cover {
    position: relative;
    width: 586px;
    height: 880px;
    overflow: hidden;
    box-shadow: 0 6px 18px rgba(0,0,0,0.25);
  }
  .cover-photo {
    position: absolute;
    inset: 0;
    background:
      radial-gradient(ellipse 45% 30% at 92% 82%, rgba(255,240,170,0.95), rgba(255,240,170,0) 70%),
      radial-gradient(ellipse 70% 40% at 60% 62%, rgba(250,248,220,0.95), rgba(250,248,220,0) 75%),
      radial-gradient(ellipse 60% 30% at 10% 8%, rgba(29,75,110,0.9), rgba(29,75,110,0) 70%),
      radial-gradient(ellipse 50% 25% at 95% 10%, rgba(40,60,90,0.85), rgba(40,60,90,0) 70%),
      radial-gradient(ellipse 40% 30% at 0% 30%, rgba(79,166,196,0.8), rgba(79,166,196,0) 70%),
      linear-gradient(180deg,
        var(--sky-deep) 0%,
        var(--cloud-light) 22%,
        var(--cloud-light) 45%,
        var(--ground-dusk) 62%,
        var(--sun-cream) 72%,
        var(--ground-green) 88%,
        #1f2b2a 100%);
  }
  .cover-text {
    position: absolute;
    inset: 0;
    text-align: center;
  }
  .cover-text > * {
    position: absolute;
    left: 0;
    right: 0;
    white-space: nowrap;
  }
  .title-line {
    font-family: "Bebas Neue", "Oswald", sans-serif;
    font-weight: 400;
    line-height: 1;
  }
  .title-hallo {
    top: 48px;
    font-size: 92px;
    color: var(--ink);
    transform: scaleX(0.78);
  }
  .title-depression {
    top: 128px;
    font-size: 140px;
    color: var(--title-blue);
    transform: scaleX(0.82);
  }
  .title-schluss {
    top: 262px;
    font-size: 98px;
    color: var(--ink);
    transform: scaleX(0.8);
  }
  .subtitle {
    top: 374px;
    font-family: "Josefin Sans", "Helvetica", sans-serif;
    text-transform: uppercase;
    color: var(--ink);
  }
  .subtitle-lead {
    font-weight: 700;
    font-size: 15px;
    letter-spacing: 0.6px;
    margin-bottom: 7px;
  }
  .subtitle-body {
    font-weight: 400;
    font-size: 12.4px;
    line-height: 19px;
  }
  .author-line {
    top: 790px;
    font-family: "Bebas Neue", "Oswald", sans-serif;
    font-size: 36px;
    line-height: 1;
    color: var(--author-white);
    transform: scaleX(0.86);
  }
</style>
</head>
<body>
  <main class="stage">
    <article class="cover">
      <div class="cover-photo" role="img" aria-label="Photograph: a person seen from behind with arms spread wide, standing on a hill in the rain as sunlight breaks through dark storm clouds"></div>
      <div class="cover-text">
        <span class="title-line title-hallo">Hallo</span>
        <span class="title-line title-depression">Depression</span>
        <span class="title-line title-schluss">Schluss!</span>
        <div class="subtitle">
          <p class="subtitle-lead">Werkzeuge für jeden Tag:</p>
          <p class="subtitle-body">
            Mit klaren Übungen &amp; Fallbeispielen aus der Praxis<br>
            Schritt für Schritt trübe Gedanken und Schwermut loslassen<br>
            Für Betroffene &amp; Familien
          </p>
        </div>
        <p class="author-line">Dipl.-Psych. Jonas Brenner &amp; Mark Feldhaus</p>
      </div>
    </article>
  </main>
</body>
</html>
```